Weight loss surgery restaurant card

We need to create a card for patients who have undergone weight loss surgery to take to restaurants so they can request smaller meals. These patients have had surgery on their stomach so that they can only consume half to one cup of food at a time. So normal sized restaurant meals are way too big (and cost a lot). This card they can present to the restaurant to communicate the fact that they have had weight loss surgery and therefore request a smaller meal portion at reduced cost

Target Market(s)

Restaurants serving weight loss surgery patients

Industry/Entity Type

Health Care

Contact Information for Business Card

This will be a plastic card similar to business card size.

Requirements
Must have
• The front of the card should include the following text:
• The individual bearing this card has undergone weight loss surgery.
• This surgery restricts portion sizes to between half and one cup of food at a time.
• Please give consideration to allowing smaller portions of your regular meals to be ordered to reduce wastage and excess costs.
• Example: a half size portion priced at two thirds of usual cost.
• The back of the card will have spaces for the person to write certain information. These are the categories that can be filled in by hand:
• Name:
• Procedure performed:
• Date of procedure (month/year):
• Treating Clinic Name:
• Treating Clinic Signature:
• Somewhere down the bottom should be something along the lines of:
• supplied from bernardwhitlow.com.au
Nice to have
• A nice design with imagery/colours etc ... not just the text on a white background! Bright attractive colours preferred.
• I have uploaded my logo ... a roughly triangular image followed by my name etc. The triangular logo image could be used somewhere on the card and this logo can be interchangeable for other clinics who purchase the card.
• **Please note that I don't want my name to be included as part of the logo on the card ... just use the triangular image on the side of the logo without the following name**
• Also, the colouring of the card does not have to reflect my logo colours as I am anticipating interchanging this logo with other logos if other clinics choose to adopt the card. I am interested to see other, more generic, colour choices as well as my logo colours

```html
<!DOCTYPE html>
<html lang="en">
<head>
<meta charset="utf-8">
<title>Weight Loss Surgery Restaurant Card</title>
<link rel="stylesheet" href="https://fonts.googleapis.com/css2?family=Caveat+Brush&family=Nunito:wght@700;800&family=Roboto+Condensed:wght@400&display=swap">
<style>
  :root {
    --page-bg: #2b2f34;
    --card-white: #ffffff;
    --teal: #0a8277;
    --teal-dark: #066b62;
    --grey-swoosh: #6d6e72;
    --box-line: #6a6a6a;
    --ink: #2a2c30;
    --board-light: #8a5632;
    --board-dark: #5b3520;
    --panel: #333b44;
    --frame: #e07a1f;
    --white-text: #ffffff;
    --red-text: #ee4242;
    --orange-text: #f07d1e;
    --green-text: #3fae4a;
    --produce-green: #6fbf3a;
    --produce-red: #e2473d;
  }
  * { box-sizing: border-box; margin: 0; padding: 0; }
  html, body {
    width: 1200px;
    height: 780px;
    overflow: hidden;
    background: var(--page-bg);
  }
  .canvas {
    position: relative;
    width: 1200px;
    height: 780px;
  }
  .card {
    position: absolute;
    top: 220px;
    width: 540px;
    height: 340px;
    border-radius: 18px;
    overflow: hidden;
    box-shadow: 0 12px 30px rgba(0,0,0,0.45);
  }

  /* Back of card: write-in details */
  .card-back {
    left: 40px;
    background: var(--card-white);
  }
  .card-back .swooshes {
    position: absolute;
    inset: 0;
  }
  .supplied-line {
    position: absolute;
    top: 20px;
    right: 30px;
    font-family: "Roboto Condensed", sans-serif;
    font-size: 17px;
    color: var(--ink);
  }
  .detail-rows {
    position: absolute;
    top: 50px;
    left: 20px;
    right: 30px;
    list-style: none;
  }
  .detail-row {
    display: flex;
    align-items: center;
    height: 32px;
    margin-bottom: 6px;
  }
  .detail-label {
    width: 210px;
    padding-right: 10px;
    text-align: right;
    font-family: "Caveat Brush", cursive;
    font-size: 19px;
    line-height: 1;
    color: var(--teal);
    white-space: nowrap;
  }
  .detail-label.is-small { font-size: 16px; }
  .write-box {
    flex: 1;
    height: 30px;
    border: 1px solid var(--box-line);
    border-radius: 7px;
    background: var(--card-white);
  }
  .clinic-mark {
    position: absolute;
    left: 20px;
    bottom: 10px;
    display: flex;
    align-items: center;
    gap: 7px;
    font-family: "Nunito", sans-serif;
    font-weight: 800;
    font-size: 13px;
    color: var(--teal);
  }
  .clinic-mark .dot {
    width: 13px;
    height: 13px;
    border-radius: 50%;
    background: var(--teal);
  }

  /* Front of card: message to restaurant */
  .card-front {
    left: 620px;
  }
  .produce-border {
    position: absolute;
    inset: 0;
    background:
      radial-gradient(circle at 12% 22%, var(--produce-red) 0 26px, transparent 27px),
      radial-gradient(circle at 90% 78%, var(--produce-red) 0 26px, transparent 27px),
      radial-gradient(circle at 14% 72%, var(--produce-green) 0 30px, transparent 31px),
      radial-gradient(circle at 88% 20%, var(--produce-green) 0 26px, transparent 27px),
      linear-gradient(90deg, var(--board-light), var(--board-dark) 50%, var(--board-light));
  }
  .message-panel {
    position: absolute;
    left: 52px;
    top: 40px;
    width: 436px;
    height: 262px;
    background: var(--panel);
    padding: 8px;
  }
  .message-frame {
    height: 100%;
    border: 1px solid var(--frame);
    display: flex;
    flex-direction: column;
    justify-content: center;
    align-items: center;
    text-align: center;
    font-family: "Nunito", sans-serif;
    font-weight: 800;
    padding: 6px 10px;
  }
  .message-frame p { line-height: 1.12; }
  .headline {
    font-size: 19px;
    color: var(--white-text);
    margin-bottom: 6px;
  }
  .headline .highlight { color: var(--red-text); }
  .restriction {
    font-size: 16px;
    color: var(--orange-text);
    padding-bottom: 4px;
    border-bottom: 1px solid var(--frame);
    margin-bottom: 6px;
  }
  .request {
    font-size: 16px;
    color: var(--red-text);
    padding-bottom: 4px;
    border-bottom: 1px solid var(--frame);
    margin-bottom: 6px;
  }
  .example {
    font-weight: 700;
    font-size: 14px;
    color: var(--green-text);
  }
</style>
</head>
<body>
<main class="canvas">

  <section class="card card-back" aria-label="Card back: patient details">
    <svg class="swooshes" width="540" height="340" viewBox="0 0 540 340" aria-hidden="true">
      <path d="M0 0 H150 C110 24 60 32 0 56 Z" fill="var(--grey-swoosh)"/>
      <path d="M0 7 H138 C100 28 55 36 0 49 Z" fill="var(--card-white)"/>
      <path d="M0 250 C110 254 150 322 270 318 C390 314 460 278 540 262 L540 282 C460 296 390 334 270 338 C160 342 110 278 0 266 Z" fill="var(--teal)"/>
    </svg>

    <p class="supplied-line">supplied from bernardwhitlow.com.au</p>

    <ul class="detail-rows">
      <li class="detail-row"><span class="detail-label">Name</span><span class="write-box"></span></li>
      <li class="detail-row"><span class="detail-label">Procedure performed</span><span class="write-box"></span></li>
      <li class="detail-row"><span class="detail-label is-small">Date of procedure (month/year)</span><span class="write-box"></span></li>
      <li class="detail-row"><span class="detail-label">Treating Clinic Name</span><span class="write-box"></span></li>
      <li class="detail-row"><span class="detail-label">Treating Clinic Signature</span><span class="write-box"></span></li>
    </ul>

    <div class="clinic-mark"><span class="dot"></span><span class="clinic-name">Meridian Clinic</span></div>
  </section>

  <section class="card card-front" aria-label="Card front: message to restaurant">
    <div class="produce-border" role="img" aria-label="Illustrated fresh vegetables and fruit on a wooden chopping board framing the card"></div>
    <div class="message-panel">
      <div class="message-frame">
        <p class="headline">The individual bearing this card<br>has undergone <span class="highlight">weight loss</span> surgery</p>
        <p class="restriction">This surgery restricts portion sizes to<br>between half and one cup of food at a time</p>
        <p class="request">Please give consideration to allowing<br>smaller portions of your regular meals to be<br>ordered to reduce wastage and excess costs.</p>
        <p class="example">Example:<br>a half size portion priced at two thirds of usual cost.</p>
      </div>
    </div>
  </section>

</main>
</body>
</html>
```